Boring Fiberglass Repair Company needs creative business cards

The Fiberglass Repair industry isn't very fun or creative but we'd like a business card that communicates a fresh, modern, and service-oriented feel. We repair bathroom fixtures (bath tubs, showers, etc) which are made out of fiberglass. Our fiberglass repair service will be sold to bathtub manufacturers and also businesses that sell bathtubs. We will also offer our services to home owners that have broken showers and bathtubs.
Target Market(s)
Home builders, plumbing wholesalers, home owners
Contact Information for Business Card
Name
Phone Number
Email Address
Business Address
Tag line: "Quality Craftsmanship Today"
Look and feel

```html
<!DOCTYPE html>
<html lang="en">
<head>
<meta charset="utf-8">
<title>Tidewell Fiberglass — Business Cards</title>
<link rel="stylesheet" href="https://fonts.googleapis.com/css2?family=Montserrat:ital,wght@0,400;0,500;0,700;0,800;1,500&display=swap">
<style>
  :root {
    --stage: #2b2c31;
    --card: #ffffff;
    --navy: #1c2e63;
    --red: #e11d27;
    --ink: #4a4a4a;
    --rule: #9a9a9a;
  }
  * { margin: 0; padding: 0; box-sizing: border-box; }
  html, body { width: 1200px; height: 800px; overflow: hidden; }
  body {
    background: var(--stage);
    font-family: "Montserrat", sans-serif;
    position: relative;
  }
  .card {
    position: absolute;
    top: 240px;
    width: 540px;
    height: 320px;
    background: var(--card);
    box-shadow: 0 18px 40px rgba(0,0,0,0.45);
    overflow: hidden;
  }
  .card--front { left: 30px; }
  .card--back { left: 630px; }

  .wordmark {
    font-family: "Montserrat", sans-serif;
    font-weight: 800;
    color: var(--navy);
    text-transform: uppercase;
    line-height: 1.05;
    letter-spacing: 0.02em;
  }
  .wordmark__line { display: block; }

  .card--front .wordmark {
    position: absolute;
    left: 0; right: 0;
    top: 92px;
    text-align: center;
    font-size: 40px;
  }
  .card--front .wordmark__line--sub { font-size: 20px; letter-spacing: 0.42em; margin-top: 6px; }
  .tagline {
    position: absolute;
    left: 0; right: 0;
    bottom: 52px;
    text-align: center;
    font-weight: 700;
    font-size: 17px;
    color: var(--navy);
  }

  .card--back .wordmark {
    position: absolute;
    left: 34px;
    top: 112px;
    font-size: 27px;
  }
  .card--back .wordmark__line--sub { font-size: 14px; letter-spacing: 0.42em; margin-top: 4px; }
  .divider {
    position: absolute;
    left: 268px;
    top: 56px;
    width: 1px;
    height: 160px;
    background: var(--rule);
  }
  .contact {
    position: absolute;
    left: 284px;
    top: 50px;
    color: var(--ink);
    font-size: 12.5px;
    line-height: 1.45;
  }
  .contact__name { font-size: 21px; font-weight: 700; color: var(--navy); line-height: 1.15; }
  .contact__name-last { color: var(--red); }
  .contact__role { font-size: 13px; margin-bottom: 4px; }
  .contact__address { margin-bottom: 4px; }
  .contact__list { list-style: none; }
  .contact__item { display: flex; align-items: center; gap: 7px; }
  .contact__icon { width: 11px; height: 11px; fill: var(--navy); flex: none; }
  .markets {
    position: absolute;
    left: 34px;
    bottom: 34px;
    font-style: italic;
    font-weight: 500;
    font-size: 14px;
    color: var(--navy);
  }
  .band { position: absolute; left: 0; bottom: 0; width: 540px; height: 32px; }
</style>
</head>
<body>
  <section class="card card--front" aria-label="Card front">
    <div class="wordmark">
      <span class="wordmark__line">Tidewell</span>
      <span class="wordmark__line wordmark__line--sub">Fiberglass</span>
    </div>
    <p class="tagline">Quality Craftsmanship Today</p>
  </section>

  <section class="card card--back" aria-label="Card back">
    <div class="wordmark">
      <span class="wordmark__line">Tidewell</span>
      <span class="wordmark__line wordmark__line--sub">Fiberglass</span>
    </div>
    <div class="divider"></div>
    <div class="contact">
      <p class="contact__name">Adrian <span class="contact__name-last">Kolvey</span></p>
      <p class="contact__role">Co-founder</p>
      <p class="contact__address">2048 Lakeside,<br>Ember Street 14-18.</p>
      <ul class="contact__list">
        <li class="contact__item">
          <svg class="contact__icon" viewBox="0 0 24 24" aria-hidden="true"><path d="M6.6 10.8a15.1 15.1 0 0 0 6.6 6.6l2.2-2.2a1 1 0 0 1 1-.25 11.4 11.4 0 0 0 3.6.57 1 1 0 0 1 1 1V20a1 1 0 0 1-1 1A17 17 0 0 1 3 4a1 1 0 0 1 1-1h3.5a1 1 0 0 1 1 1c0 1.25.2 2.45.57 3.6a1 1 0 0 1-.25 1z"/></svg>
          +36.1.555.0142
        </li>
        <li class="contact__item">
          <svg class="contact__icon" viewBox="0 0 24 24" aria-hidden="true"><rect x="7" y="2" width="10" height="20" rx="2"/></svg>
          +36.30.555.0187
        </li>
        <li class="contact__item">
          <svg class="contact__icon" viewBox="0 0 24 24" aria-hidden="true"><path d="M2 5h20v14H2zM3 6l9 7 9-7" stroke="#fff" stroke-width="1.5"/></svg>
          hello@tidewellfiberglass.com
        </li>
        <li class="contact__item">
          <svg class="contact__icon" viewBox="0 0 24 24" aria-hidden="true"><circle cx="12" cy="12" r="10"/></svg>
          www.tidewellfiberglass.com
        </li>
      </ul>
    </div>
    <p class="markets">Home builders, plumbing wholesalers, home owners</p>
    <svg class="band" viewBox="0 0 540 32" preserveAspectRatio="none" aria-hidden="true">
      <polygon points="0,27 310,15 300,32 0,32" fill="var(--navy)"/>
      <polygon points="316,15 540,6 540,32 306,32" fill="var(--red)"/>
    </svg>
  </section>
</body>
</html>
```